Business Card Design

We recently had a new logo designed by Pixel Harbor. Now we want to create new business cards and letterhead that compliment our new logo.

We are audiologists in private practice specializing in hearing evaluations and fitting hearing aids. We want a clean and professional card.

We need business cards for each audiologist. The names and titles are:
Marlene Voss-Kettering, AuD
Audiologist

Jane Pratt, AuD
Audiologist

Corinna Lundt, AuD
Audiologist

We also need a business card with no provider. Just a generic one.

Finally, we need an appointment card. This is what the front desk uses to give to the patient with their next appointment date and time.

Target Market(s)

Our clients tend to be highly educated. They are older so the cards should be clean and easy to read. No squirrely font please.

Industry/Entity Type

Business

Contact Information for Business Card

27831 Birchmont Dr NE, suite 418
Seattle, WA 98177
206-555-0182

Requirements
Must have
• Clean
Easy to read
Professional
Modern but approachable / warm
Should not have
• Other pictures besides the logo

```html
<!DOCTYPE html>
<html lang="en">
<head>
<meta charset="utf-8">
<title>Eastbrook Hearing Services – Business &amp; Appointment Cards</title>
<link href="https://fonts.googleapis.com/css2?family=Montserrat:wght@600;700&family=Lato:wght@400;700&family=Libre+Baskerville:ital@0;1&display=swap" rel="stylesheet">
<style>
  :root {
    --stage: #2b2b2d;
    --card: #fbfbfb;
    --ink: #2a2a2c;
    --muted: #6a6a6e;
    --teal: #2f9e8c;
    --teal-light: #5cc0ad;
    --navy: #2e4a6b;
    --rule: #3a3a3c;
  }
  * { margin: 0; padding: 0; box-sizing: border-box; }
  html, body { width: 1200px; height: 873px; overflow: hidden; }
  body {
    background: var(--stage);
    position: relative;
    font-family: "Lato", Arial, sans-serif;
    color: var(--ink);
  }
  .card {
    position: absolute;
    width: 520px;
    height: 300px;
    background: var(--card);
    border-radius: 18px;
    box-shadow: 0 14px 30px rgba(0,0,0,.45);
    overflow: hidden;
  }
  .card--appointment { left: 55px; top: 286px; }
  .card--business { left: 625px; top: 286px; }

  /* brand lockup */
  .brand { display: flex; align-items: center; gap: 12px; }
  .brand__dot { width: 46px; height: 46px; border-radius: 50%; background: var(--navy); flex: none; }
  .brand__name {
    font-family: "Montserrat", Arial, sans-serif;
    font-weight: 700;
    color: var(--ink);
    text-transform: uppercase;
    line-height: 1.1;
    letter-spacing: .5px;
  }
  .brand__tagline { font-size: 11px; color: var(--muted); margin-top: 3px; letter-spacing: .4px; white-space: nowrap; }

  /* appointment card */
  .card--appointment .brand { position: absolute; right: 28px; top: 24px; text-align: right; }
  .card--appointment .brand__name { font-size: 15px; }
  .card--appointment .brand__tagline { font-size: 9px; }
  .appointment__badge {
    position: absolute; left: 0; top: 140px;
    width: 250px; height: 32px;
    background: var(--teal-light);
    border-radius: 0 16px 16px 0;
    color: #fff;
    font-family: "Libre Baskerville", Georgia, serif;
    font-size: 11.5px; letter-spacing: 1.2px;
    white-space: nowrap;
    display: flex; align-items: center; padding-left: 22px;
  }
  .field { position: absolute; border-bottom: 1.5px solid var(--rule); height: 26px; }
  .field__label {
    position: absolute; bottom: 5px;
    font-family: "Libre Baskerville", Georgia, serif;
    font-style: italic; font-size: 13px;
    white-space: nowrap;
  }
  .field--patient { left: 150px; right: 28px; top: 92px; }
  .field--patient .field__label { left: 120px; color: #9a9a9e; }
  .field--time { left: 270px; right: 28px; top: 178px; }
  .field--time .field__label { left: 60px; color: var(--teal); }
  .field--date { left: 28px; right: 28px; top: 238px; }
  .field--date .field__label { left: 0; color: var(--teal); }

  /* business card */
  .card--business .brand { position: absolute; left: 120px; top: 30px; }
  .card--business .brand__name { font-size: 20px; }
  .rule { position: absolute; height: 2px; background: var(--teal); }
  .rule--top { left: 150px; right: 28px; top: 108px; }
  .rule--bottom { left: 28px; width: 190px; top: 182px; }
  .person { position: absolute; right: 30px; top: 120px; text-align: right; }
  .person__name { font-family: "Montserrat", Arial, sans-serif; font-weight: 700; font-size: 17px; }
  .person__title { font-size: 12px; color: var(--muted); margin-top: 2px; }
  .address {
    position: absolute; right: 30px; top: 176px; text-align: right;
    color: var(--teal); font-weight: 700; font-size: 13px; line-height: 1.35;
  }
  .contacts { position: absolute; left: 28px; top: 192px; list-style: none; }
  .contacts li {
    display: flex; align-items: center; gap: 12px;
    font-size: 12.5px; font-weight: 700; height: 24px;
  }
  .contacts svg { width: 15px; height: 15px; flex: none; fill: none; stroke: var(--teal); stroke-width: 1.8; }
  .contacts svg .solid { fill: var(--teal); stroke: none; }
</style>
</head>
<body>

<section class="card card--appointment" aria-label="Appointment card">
  <div class="brand">
    <div>
      <div class="brand__name">Eastbrook<br>Hearing Services</div>
      <div class="brand__tagline">Clear care for every conversation</div>
    </div>
  </div>
  <div class="field field--patient"><span class="field__label">Patient Name</span></div>
  <div class="appointment__badge">YOUR NEXT APPOINTMENT</div>
  <div class="field field--time"><span class="field__label">Time:</span></div>
  <div class="field field--date"><span class="field__label">Date:</span></div>
</section>

<section class="card card--business" aria-label="Business card">
  <div class="brand">
    <span class="brand__dot"></span>
    <div>
      <div class="brand__name">Eastbrook<br>Hearing Services</div>
      <div class="brand__tagline">Clear care for every conversation</div>
    </div>
  </div>
  <div class="rule rule--top"></div>
  <div class="person">
    <div class="person__name">Marlene Voss-Kettering, AuD</div>
    <div class="person__title">Audiologist</div>
  </div>
  <div class="address">27831 Birchmont Dr NE, Suite 418<br>Seattle WA 98177</div>
  <div class="rule rule--bottom"></div>
  <ul class="contacts">
    <li><svg viewBox="0 0 16 16"><rect x="4" y="1.5" width="8" height="13" rx="1.5"/></svg>(206) 555-0182</li>
    <li><svg viewBox="0 0 16 16"><rect class="solid" x="1" y="6" width="14" height="6" rx="1"/><rect x="4" y="2" width="8" height="4"/><rect x="4" y="10" width="8" height="4"/></svg>206-555-0147</li>
    <li><svg viewBox="0 0 16 16"><rect class="solid" x="1" y="3" width="14" height="10" rx="1"/><path d="M1.5 3.5 8 9l6.5-5.5" stroke="#fff"/></svg>info@eastbrookhearing.com</li>
    <li><svg viewBox="0 0 16 16"><path d="M7 9.5 9.5 7M6 7.5 4 9.5a2.1 2.1 0 0 0 3 3l2-2M10 8.5l2-2a2.1 2.1 0 0 0-3-3l-2 2"/></svg>www.eastbrookhearing.com</li>
  </ul>
</section>

</body>
</html>
```